Business card for someone who trains leaders
Organizational Development Consultant Business Card - Consulting
Organizational Development Consultant Business Card
Bright & Fun-filled
Darla Quinby
Capacity Development Adviser
(NO ADDRESS IS LISTED ON CARD)
darla@vrmthrivewell.com
www.netprofile/in/marlowquinby
I want a business card that says professional but not too corporate. I want it to only use the colors on my logo (plus white of course). I like the look of cards that have some black backgrounds, but I'm open to a lot of different looks - as long as it meshes well with the look and feel of the business card. I don't want anything too busy, but yet want something that stands out a bit.
Where Will Your Growth Lead? Let VRM Thrivewell help you find growth through organizational development, leadership coaching, and much more!
marlowquinby marlowquinby
Please don't submit generic samples with someone else's information. I'm only interested in seeing completed business cards with the information I included in the creative brief.
I would like to see some designs that are on a white background as well as a black background. I'm not sold either way, but want to see a variety. Also, on the creative brief, I left off the website. In addition to my netprofile profile, I also want the website www.vrmthrivewell.com.

```html
<!DOCTYPE html>
<html lang="en">
<head>
<meta charset="utf-8">
<title>VRM Thrivewell Business Cards</title>
<link rel="stylesheet" href="https://fonts.googleapis.com/css2?family=Open+Sans:wght@400;600;700&family=Roboto+Condensed:wght@400;700&display=swap">
<style>
  :root {
    --bg: #8a8a8c;
    --card-black: #0d0d0f;
    --card-white: #ffffff;
    --purple: #6b3fa3;
    --purple-soft: #8e63c4;
    --blue: #2b86d4;
    --gray-faint: #e6e4ea;
    --ink: #3a3a3e;
    --white: #ffffff;
  }
  * { box-sizing: border-box; margin: 0; padding: 0; }
  html, body { width: 1200px; height: 908px; overflow: hidden; }
  body {
    background: var(--bg);
    font-family: "Open Sans", Arial, sans-serif;
    position: relative;
  }
  .card {
    position: absolute;
    width: 560px;
    height: 320px;
    border-radius: 14px;
    overflow: hidden;
    box-shadow: 0 10px 24px rgba(0,0,0,0.35);
  }
  /* Front card (black) */
  .card--front {
    left: 40px; top: 110px;
    background: linear-gradient(135deg, #1c1c20 0%, var(--card-black) 60%);
    color: var(--white);
  }
  .front__brand {
    position: absolute; left: 34px; top: 112px;
    font-family: "Roboto Condensed", Arial, sans-serif;
    font-weight: 700; font-size: 30px; letter-spacing: 0.5px;
    color: var(--blue);
  }
  .front__tagline {
    position: absolute; left: 36px; top: 152px;
    font-size: 12px; color: #d8d8dc;
  }
  .front__blurb {
    position: absolute; left: 36px; top: 182px; width: 270px;
    font-size: 13px; line-height: 1.45; font-weight: 600; color: var(--white);
  }
  .front__mark {
    position: absolute; right: 40px; top: 40px;
    width: 230px; height: 230px; border-radius: 50%;
    background: var(--purple);
  }
  /* Back card (white) */
  .card--back {
    left: 600px; top: 470px;
    background: var(--card-white);
    color: var(--ink);
  }
  .back__corner {
    position: absolute; left: 0; top: 0;
    width: 46px; height: 34px; background: var(--blue);
  }
  .back__watermark {
    position: absolute; right: 30px; top: 18px;
    width: 190px; height: 190px; border-radius: 50%;
    background: var(--gray-faint);
  }
  .back__brand {
    position: absolute; left: 30px; top: 92px;
    display: flex; align-items: center; gap: 12px;
  }
  .back__brand-dot {
    width: 46px; height: 46px; border-radius: 50%; background: var(--purple);
  }
  .back__brand-name {
    font-family: "Roboto Condensed", Arial, sans-serif;
    font-weight: 700; font-size: 24px; color: var(--blue);
  }
  .back__brand-tagline {
    font-size: 10px; color: #6a6a70; margin-top: 2px;
  }
  .back__band {
    position: absolute; left: 0; bottom: 50px;
    width: 270px; height: 44px; background: var(--purple);
  }
  .back__person {
    position: absolute; left: 290px; top: 160px;
  }
  .back__name {
    font-size: 17px; font-weight: 700; color: var(--blue);
  }
  .back__title {
    font-size: 12px; font-weight: 600; color: var(--purple); margin-bottom: 10px;
  }
  .contact-list { list-style: none; }
  .contact-list li {
    display: flex; align-items: center; gap: 7px;
    font-size: 11px; line-height: 1.75; color: var(--ink);
  }
  .contact-list svg { width: 11px; height: 11px; flex: none; }
</style>
</head>
<body>

  <section class="card card--front" aria-label="Business card front">
    <div class="front__mark" aria-hidden="true"></div>
    <div class="front__brand">VRM THRIVEWELL</div>
    <div class="front__tagline">Where Will Your Growth Lead?</div>
    <p class="front__blurb">Let VRM Thrivewell help you find growth through organizational development, leadership coaching, and much more!</p>
  </section>

  <section class="card card--back" aria-label="Business card back">
    <div class="back__corner" aria-hidden="true"></div>
    <div class="back__watermark" aria-hidden="true"></div>
    <div class="back__brand">
      <div class="back__brand-dot" aria-hidden="true"></div>
      <div>
        <div class="back__brand-name">VRM THRIVEWELL</div>
        <div class="back__brand-tagline">Where Will Your Growth Lead?</div>
      </div>
    </div>
    <div class="back__band" aria-hidden="true"></div>
    <div class="back__person">
      <div class="back__name">Darla Quinby</div>
      <div class="back__title">Capacity Development Adviser</div>
      <ul class="contact-list">
        <li>
          <svg viewBox="0 0 12 12" aria-hidden="true"><path d="M3 1 L5 3.5 L4 5 Q5.5 7 7 8 L8.5 7 L11 9 L9.5 11 Q4 10 1 2.5 Z" fill="#6b3fa3"/></svg>
          555-014-2287
        </li>
        <li>
          <svg viewBox="0 0 12 12" aria-hidden="true"><rect x="1" y="2.5" width="10" height="7" rx="1" fill="#6b3fa3"/><path d="M1.5 3 L6 6.5 L10.5 3" stroke="#fff" fill="none"/></svg>
          darla@vrmthrivewell.com
        </li>
        <li>
          <svg viewBox="0 0 12 12" aria-hidden="true"><rect x="1" y="1" width="10" height="10" rx="2" fill="#6b3fa3"/></svg>
          www.netprofile/in/marlowquinby
        </li>
        <li>
          <svg viewBox="0 0 12 12" aria-hidden="true"><circle cx="6" cy="6" r="5" fill="none" stroke="#6b3fa3" stroke-width="1.3"/><path d="M1 6 H11 M6 1 Q3 6 6 11 Q9 6 6 1" fill="none" stroke="#6b3fa3" stroke-width="1"/></svg>
          www.vrmthrivewell.com
        </li>
      </ul>
    </div>
  </section>

</body>
</html>
```